Cover Art Needed For Digital Single Release

We are looking to have the cover art designed for a new song called "Paper Lanterns". You will find the track attached below in a private Tunepool link so that you can have a listen.
We are thinking of keeping the artwork fairly simple but still want it to catch your eye. Maybe using the song title and artist’s name in a colorful and creative way. (A well-designed font with a bold color scheme, or even something like a mosaic style art piece featuring the title).
We completely welcome any and all creative visions you might have, even if it strays away from the examples given above.
Thank you in advance for your submissions, and we are excited to collaborate with you!
"Paper Lanterns" by Marcus Fell
https://tunepool.example/marcuszxq/paper-lanterns/s-r7tWnexiLqa
Target Market(s)
Teens/Young Adults
Industry/Entity Type
Music
Requirements
Must have
- An eye-catching design
Should not have
- Please do not rely heavily on stock images. We prefer an original design/concept.

```html
<!DOCTYPE html>
<html lang="en">
<head>
<meta charset="utf-8">
<title>Paper Lanterns — Marcus Fell</title>
<link rel="stylesheet" href="https://fonts.googleapis.com/css2?family=Caveat+Brush&family=Caveat:wght@600&display=swap">
<style>
  :root {
    --ink: #000000;
    --bloom-core: #fb0a05;
    --bloom-mid: #ee0a38;
    --bloom-edge: #c80e48;
    --glass-magenta: #c030c8;
    --glass-sky: #0cb4f8;
    --glass-mint: #0cf67a;
    --glass-lime: #3cf60c;
    --glass-navy: #140a88;
    --glass-olive: #6e9e10;
    --glass-grey: #909a8c;
    --glass-plum: #a00c50;
  }
  html, body {
    margin: 0;
    padding: 0;
    width: 1200px;
    height: 1200px;
    overflow: hidden;
    background: var(--glass-sky);
  }
  .cover {
    position: relative;
    width: 1200px;
    height: 1200px;
    overflow: hidden;
  }
  .cover-artwork {
    position: absolute;
    inset: 0;
    background:
      radial-gradient(ellipse 44% 42% at 48% 50%, var(--bloom-core) 0%, var(--bloom-mid) 60%, rgba(238,10,56,0) 100%),
      radial-gradient(ellipse 62% 60% at 50% 52%, var(--bloom-mid) 0%, var(--bloom-edge) 70%, rgba(200,14,72,0) 100%),
      radial-gradient(circle at 3% 5%, var(--glass-grey) 0%, rgba(144,154,140,0) 14%),
      radial-gradient(circle at 22% 6%, var(--glass-navy) 0%, rgba(20,10,136,0) 12%),
      radial-gradient(circle at 0% 30%, var(--glass-magenta) 0%, rgba(192,48,200,0) 16%),
      radial-gradient(circle at 0% 55%, var(--glass-sky) 0%, rgba(12,180,248,0) 18%),
      radial-gradient(circle at 0% 92%, var(--glass-mint) 0%, rgba(12,246,122,0) 22%),
      radial-gradient(circle at 50% 100%, var(--glass-lime) 0%, rgba(60,246,12,0) 14%),
      radial-gradient(circle at 100% 5%, var(--glass-sky) 0%, rgba(12,180,248,0) 16%),
      radial-gradient(circle at 100% 40%, var(--glass-olive) 0%, rgba(110,158,16,0) 14%),
      radial-gradient(circle at 100% 72%, var(--glass-lime) 0%, rgba(60,246,12,0) 16%),
      radial-gradient(circle at 98% 98%, var(--glass-plum) 0%, rgba(160,12,80,0) 16%),
      var(--glass-magenta);
  }
  .single-title {
    position: absolute;
    inset: 0;
    margin: 0;
    font-family: "Caveat Brush", cursive;
    font-weight: 400;
    color: var(--ink);
    line-height: 1;
  }
  .title-line {
    position: absolute;
    white-space: nowrap;
  }
  .title-line--first {
    left: 70px;
    top: 120px;
    font-size: 430px;
    transform: rotate(-4deg);
  }
  .title-line--second {
    left: 290px;
    top: 560px;
    font-size: 270px;
    transform: rotate(-3deg);
  }
  .artist-name {
    position: absolute;
    left: 686px;
    top: 822px;
    margin: 0;
    font-family: "Caveat", cursive;
    font-weight: 600;
    font-size: 88px;
    color: var(--ink);
    line-height: 1;
    white-space: nowrap;
  }
</style>
</head>
<body>
  <main class="cover">
    <div class="cover-artwork" role="img" aria-label="Stained-glass mosaic of bright coloured panes around a large red flower at the centre"></div>

    <h1 class="single-title">
      <span class="title-line title-line--first">Paper</span>
      <span class="title-line title-line--second">Lanterns</span>
    </h1>
    <p class="artist-name">Marcus Fell</p>
  </main>
</body>
</html>
```